Vardek Hub, LLC. is the name of the company that will be an Internet startup working in E-commerce and

We are a new company and going to start the business by hiring people we need. We are on “Hiring Now…” status right now which we like to be displayed on the website homepage.
The website should allow us to start the hiring process with letting people see and apply for jobs posted on the website.

the company logo is attached.

Target Market(s)

Tech Job Seekers, Programmers, iOS and Android Developers, Software engineers, Graphic designers, QA engineers, Customer Service Reps,...

Industry/Entity Type

Internet

Number of Pages Required

5+ page

Font styles to use
Serif
Sans Serif

Colors

Designer to choose colors to be used in the design.

Requirements
Must have
• We need a system to help job seekers to upload the resume and cover letter and fill the required forms and answer some questions on a form designed to evaluate the job seekers and let them know if they fit in the position and should apply for it.
• We also want job seekers to do a Pre-Employment Tests including Aptitude, Personality, and Skills after they qualified for a job which links our website to web-based pre-employment testing services websites like (Quorva, Pellmark, Brumhall & Associates, Tolvin Assessment, …)

```html
<!DOCTYPE html>
<html lang="en">
<head>
<meta charset="utf-8">
<title>Vardek Hub — Hiring Now</title>
<link href="https://fonts.googleapis.com/css2?family=Cinzel:wght@700;900&family=Mulish:ital,wght@0,300;0,400;0,600;0,700;1,400;1,600&display=swap" rel="stylesheet">
<style>
:root{
  --teal:#3bbccb;
  --teal-dark:#2aa3b3;
  --orange:#ff5a1a;
  --orange-soft:#ff7a3d;
  --blue:#2c8fc7;
  --ink:#333;
  --muted:#666;
  --white:#fff;
  --black:#0b0b0b;
  --line:#e2e2e2;
}
*{box-sizing:border-box;margin:0;padding:0}
html,body{width:1200px;height:4412px;overflow:hidden}
body{position:relative;font-family:"Mulish",Arial,sans-serif;color:var(--ink);background:var(--white)}
section,header,footer{position:absolute;left:0;width:1200px;overflow:hidden}
.btn{display:inline-block;border-radius:30px;font-family:"Mulish",sans-serif;font-weight:600;font-size:22px;letter-spacing:.5px;text-transform:uppercase;padding:14px 34px;color:var(--white);background:var(--orange);text-decoration:none}
.btn--blue{background:var(--blue)}
.btn--ghost{background:transparent;border:2px solid var(--white)}
.btn--outline{background:var(--white);border:2px solid var(--orange);color:var(--orange)}
.section-title{font-weight:300;font-size:46px;text-transform:uppercase;color:var(--teal);text-align:center;letter-spacing:1px}
.section-title span{color:var(--orange)}
.title-rule{width:60px;height:3px;background:var(--ink);margin:14px auto 0}
.body-copy{font-size:15px;line-height:26px;color:var(--muted)}
.photo{position:absolute}

/* header */
.site-header{top:0;height:100px;background:var(--white)}
.brand{position:absolute;left:60px;top:22px;display:flex;align-items:center;gap:12px}
.brand__name{font-size:40px;font-weight:700;color:var(--blue);letter-spacing:-.5px}
.brand__dot{width:22px;height:22px;border-radius:50%;background:var(--orange)}
.main-nav{position:absolute;left:384px;top:42px;display:flex;gap:30px;font-size:17px;text-transform:uppercase;color:var(--ink)}
.main-nav .is-active{color:var(--teal)}
.header-cta{position:absolute;left:934px;top:28px;padding:10px 26px;font-size:20px}

/* hero */
.hero{top:100px;height:576px}
.hero__photo{left:0;top:0;width:1200px;height:576px;background:linear-gradient(100deg,#bfd3dc 0%,#8fb0bd 40%,#5a6f7a 65%,#d7e3e8 100%)}
.hero__title{position:absolute;left:72px;top:176px;font-family:"Cinzel",serif;font-weight:900;font-size:64px;color:var(--white);letter-spacing:1px}
.hero__text{position:absolute;left:80px;top:272px;width:500px;font-size:16px;line-height:26px;font-style:italic;font-weight:600;color:var(--white)}
.hero__actions{position:absolute;left:80px;top:364px;display:flex;gap:14px}
.hero__actions .btn{padding:16px 28px}
.hero__arrow{position:absolute;top:272px}
.apply-form{position:absolute;left:770px;top:6px;width:348px;height:364px;background:var(--white);padding:22px 18px}
.apply-form__field{height:44px;background:#ededed;margin-bottom:10px;font-size:13px;color:#777;padding:14px 18px;position:relative}
.apply-form__field svg{position:absolute;right:14px;top:14px}
.apply-form .btn{display:block;width:180px;margin:10px auto 0;text-align:center;padding:14px 0}

/* welcome */
.welcome{top:676px;height:397px;text-align:center}
.welcome .section-title{margin-top:62px}
.welcome .body-copy{width:960px;margin:22px auto 0}
.welcome .body-copy + .body-copy{margin-top:10px}
.welcome .btn{margin-top:22px}

/* process */
.process{top:1073px;height:735px}
.process__bg{left:0;top:0;width:1200px;height:735px;background:linear-gradient(90deg,#58c2cf 0%,#67c8d3 55%,#7ad0d8 100%)}
.process__person{left:700px;top:150px;width:380px;height:500px;background:radial-gradient(ellipse at center,#c9a68b 0%,#8aa4b8 55%,rgba(122,208,216,0) 75%)}
.process .section-title{position:absolute;left:78px;top:80px;color:var(--white);text-align:left}
.process__rule{position:absolute;left:78px;top:144px;width:60px;height:3px;background:var(--white)}
.step{position:absolute;display:flex;align-items:center;gap:18px}
.step__icon{width:124px;height:124px;border-radius:50%;border:6px solid var(--white);display:flex;align-items:center;justify-content:center}
.step__name{font-size:18px;text-transform:uppercase;color:var(--white);letter-spacing:.5px}
.step__name--hi{color:var(--orange)}
.step__text{font-size:14px;line-height:22px;color:var(--white);width:330px;margin-top:4px}

/* banner */
.banner{top:1808px;height:156px;background:var(--orange)}
.banner__title{position:absolute;left:78px;top:36px;font-size:23px;font-style:italic;font-weight:600;color:var(--white)}
.banner__text{position:absolute;left:78px;top:76px;width:840px;font-size:14px;line-height:24px;color:var(--white)}
.banner .btn{position:absolute;left:936px;top:46px;padding:14px 36px}

/* about */
.about{top:1964px;height:520px}
.about__photo{left:0;top:0;width:1200px;height:520px;background:linear-gradient(90deg,#6d7a86 0%,#8d9aa4 40%,#4d97ad 70%,#3f93ab 100%)}
.about .section-title{position:absolute;left:608px;top:60px;color:var(--white)}
.about__rule{position:absolute;left:608px;top:124px;width:60px;height:3px;background:var(--white)}
.about .body-copy{position:absolute;left:608px;width:500px;color:var(--white);font-size:14px;line-height:24px}
.about .btn{position:absolute;left:608px;top:382px}

/* services */
.services{top:2484px;height:544px;text-align:center}
.services .section-title{margin-top:68px}
.services .body-copy{width:860px;margin:20px auto 0}
.service-grid{position:absolute;left:80px;top:215px;width:1040px;height:265px;display:flex}
.service-card{flex:1;position:relative}
.service-card__label{position:absolute;left:0;right:0;bottom:18px;font-size:17px;color:var(--white);text-transform:uppercase;text-align:center}
.service-card__icon{position:absolute;left:90px;top:40px}

/* newsletter */
.newsletter{top:3028px;height:303px;background:linear-gradient(90deg,#2a8bc4,#3397cc);text-align:center}
.newsletter .section-title{margin-top:54px;color:var(--white)}
.newsletter__sub{color:var(--white);font-size:15px;margin-top:14px}
.newsletter__form{position:absolute;left:206px;top:180px;display:flex;gap:14px}
.newsletter__input{width:314px;height:58px;background:var(--white);font-size:14px;color:#888;text-align:left;padding:20px 14px}
.newsletter .btn{padding:18px 30px;font-size:20px}

/* news */
.news{top:3331px;height:338px}
.news .section-title{margin-top:60px}
.news-item{position:absolute;top:152px;display:flex;gap:24px}
.news-item__thumb{width:130px;height:110px;border:2px solid var(--line);background:linear-gradient(135deg,#d6cfc6,#7d7a78)}
.news-item__title{font-size:17px;font-weight:700;color:var(--ink)}
.news-item__text{font-size:14px;line-height:23px;color:var(--muted);width:280px;margin-top:8px}
.news-item__meta{display:flex;gap:14px;align-items:center;font-size:13px;color:var(--orange);margin-top:10px}

/* career */
.career{top:3669px;height:417px}
.career__bg{left:0;top:0;width:1200px;height:417px;background:linear-gradient(90deg,#f1f7f7 0%,#dbeeee 60%,#c9e6e6 100%)}
.career__person{left:830px;top:30px;width:300px;height:387px;background:linear-gradient(180deg,#c79a7f 0%,#9e6f5a 30%,#c8c1ba 60%,#5d6e83 100%);border-radius:140px 140px 0 0}
.career .section-title{position:absolute;left:78px;top:58px;text-align:left}
.career__rule{position:absolute;left:78px;top:122px;width:60px;height:3px;background:var(--ink)}
.career .body-copy{position:absolute;left:78px;top:140px;width:700px;font-size:14px;line-height:24px}
.career__actions{position:absolute;left:78px;top:205px;display:flex;gap:10px}
.career__actions .btn{padding:16px 26px;font-size:20px}

/* footer */
.site-footer{top:4086px;height:326px;background:var(--black);text-align:center}
.footer-brand{position:absolute;left:0;right:0;top:44px;display:flex;justify-content:center;align-items:center;gap:12px}
.footer-brand .brand__name{font-size:56px}
.social{position:absolute;left:0;right:0;top:160px;display:flex;justify-content:center;gap:12px}
.social__item{width:44px;height:44px;border-radius:50%;background:var(--orange)}
.footer-nav{position:absolute;left:0;right:0;top:238px;display:flex;justify-content:center;gap:34px;font-size:14px;color:#ccc}
.footer-legal{position:absolute;left:0;right:0;top:270px;font-size:13px;color:#bbb}
.footer-legal b{color:var(--orange);font-weight:600}
</style>
</head>
<body>

<header class="site-header">
  <div class="brand"><span class="brand__name">Vardek Hub</span><span class="brand__dot"></span></div>
  <nav class="main-nav">
    <span class="is-active">Home ▾</span><span>About</span><span>Services</span><span>Career</span><span>News</span><span>Contact</span>
  </nav>
  <a class="btn header-cta">Join with us</a>
</header>

<section class="hero">
  <div class="photo hero__photo" role="img" aria-label="Business person in a suit giving a thumbs up in a bright office"></div>
  <svg class="hero__arrow" style="left:24px" width="20" height="40" viewBox="0 0 20 40"><path d="M16 4 4 20l12 16" fill="none" stroke="#fff" stroke-width="3"/></svg>
  <svg class="hero__arrow" style="left:1156px" width="20" height="40" viewBox="0 0 20 40"><path d="M4 4l12 16L4 36" fill="none" stroke="#fff" stroke-width="3"/></svg>
  <h1 class="hero__title">Hiring Now......</h1>
  <p class="hero__text">Tech Job Seekers, Programmers, iOS and Android Developers, Software engineers, Graphic designers, QA engineers, Customer Service Reps...</p>
  <div class="hero__actions"><a class="btn btn--blue">Learn more</a><a class="btn">Apply now</a></div>
  <form class="apply-form">
    <div class="apply-form__field">Name *</div>
    <div class="apply-form__field">Email *</div>
    <div class="apply-form__field">Post *<svg width="14" height="10" viewBox="0 0 14 10"><path d="M0 0h14L7 10z" fill="#ff5a1a"/></svg></div>
    <div class="apply-form__field">Coverletter *<svg width="14" height="16" viewBox="0 0 14 16"><path d="M10 4 4 10a2 2 0 0 0 3 3l6-6a4 4 0 0 0-6-6L1 7" fill="none" stroke="#ff5a1a" stroke-width="1.6"/></svg></div>
    <div class="apply-form__field">Resume *<svg width="14" height="16" viewBox="0 0 14 16"><path d="M10 4 4 10a2 2 0 0 0 3 3l6-6a4 4 0 0 0-6-6L1 7" fill="none" stroke="#ff5a1a" stroke-width="1.6"/></svg></div>
    <a class="btn">Apply now</a>
  </form>
</section>

<section class="welcome">
  <h2 class="section-title">Welcome to <span>Vardek Hub</span></h2>
  <div class="title-rule"></div>
  <p class="body-copy">Lorem Ipsum is simply dummy text of the printing and typesetting industry. Lorem Ipsum has been the industry's standard dummy text ever since the 1500s, when an unknown printer took a galley of type and scrambled.</p>
  <p class="body-copy">Lorem Ipsum is simply dummy text of the printing and typesetting industry. Lorem Ipsum has been the industry's standard dummy text ever since the 1500s, when an unknown printer took a galley of type and scrambled it to make a type specimen book. It has survived not only five centuries, but also the leap into electronic typesetting, remaining essentially unchanged.</p>
  <a class="btn">Learn more</a>
</section>

<section class="process">
  <div class="photo process__bg" role="img" aria-label="Soft teal office backdrop"></div>
  <div class="photo process__person" role="img" aria-label="Young man with glasses sitting cross-legged using a tablet"></div>
  <h2 class="section-title">Vardek Hub <span>Hiring Process</span></h2>
  <div class="process__rule"></div>

  <div class="step" style="left:244px;top:152px">
    <div class="step__icon" style="background:var(--orange)">
      <svg width="54" height="54" viewBox="0 0 54 54" fill="none" stroke="#fff" stroke-width="3"><rect x="8" y="10" width="38" height="26" rx="2"/><path d="M20 46h14M27 36v10M16 20h22M16 27h14"/></svg>
    </div>
    <div><div class="step__name step__name--hi">Aptitude Test</div><p class="step__text">Lorem Ipsum is simply dummy text of the printing and typesetting industry.</p></div>
  </div>
  <div class="step" style="left:118px;top:273px">
    <div class="step__icon" style="background:var(--teal)">
      <svg width="54" height="54" viewBox="0 0 54 54" fill="none" stroke="#fff" stroke-width="3"><circle cx="27" cy="19" r="10"/><path d="M9 48c2-11 9-16 18-16s16 5 18 16"/></svg>
    </div>
    <div><div class="step__name">Personality</div><p class="step__text">Lorem Ipsum is simply dummy text of the printing and typesetting industry.</p></div>
  </div>
  <div class="step" style="left:118px;top:400px">
    <div class="step__icon" style="background:var(--blue)">
      <svg width="54" height="54" viewBox="0 0 54 54" fill="none" stroke="#fff" stroke-width="3"><rect x="12" y="6" width="30" height="42" rx="2"/><path d="M18 16h18M18 24h18M18 32h18M18 40h10"/></svg>
    </div>
    <div><div class="step__name">Skills</div><p class="step__text">Lorem Ipsum is simply dummy text of the printing and typesetting industry.</p></div>
  </div>
  <div class="step" style="left:244px;top:527px">
    <div class="step__icon" style="background:#555">
      <svg width="54" height="54" viewBox="0 0 54 54" fill="none" stroke="#fff" stroke-width="3"><rect x="6" y="10" width="42" height="30" rx="2"/><path d="M14 20h16M14 28h10"/><circle cx="38" cy="36" r="7"/><path d="M35 36l2 2 4-4"/></svg>
    </div>
    <div><div class="step__name">Qualified</div><p class="step__text">Lorem Ipsum is simply dummy text of the printing and typesetting industry.</p></div>
  </div>
</section>

<section class="banner">
  <h3 class="banner__title">We Are Vardek Hub, Easy Way To do Pre-Employment Tests For Job seekers.</h3>
  <p class="banner__text">Lorem Ipsum is simply dummy text of the printing and typesetting industry. Lorem Ipsum has been the industry's standard dummy text ever since the 1500s, when an unknown printer took a galley of type and scrambled.</p>
  <a class="btn btn--ghost">Apply now</a>
</section>

<section class="about">
  <div class="photo about__photo" role="img" aria-label="Smiling man working on a laptop at a desk"></div>
  <h2 class="section-title">About <span>Us</span></h2>
  <div class="about__rule"></div>
  <p class="body-copy" style="top:140px">Lorem Ipsum is simply dummy text of the printing and typesetting industry. Lorem Ipsum has been the industry's standard dummy text ever since the 1500s, when an unknown printer took a galley of type and scrambled.</p>
  <p class="body-copy" style="top:236px">Lorem Ipsum is simply dummy text of the printing and typesetting industry. Lorem Ipsum has been the industry's standard dummy text ever since the 1500s, when an unknown printer took a galley of type and scrambled it to make a type specimen book. It has survived not only five centuries, but also the leap into electronic typesetting, remaining essentially unchanged.</p>
  <a class="btn">Learn more</a>
</section>

<section class="services">
  <h2 class="section-title">Our Best <span>Services</span></h2>
  <div class="title-rule"></div>
  <p class="body-copy">Lorem Ipsum is simply dummy text of the printing and typesetting industry. Lorem Ipsum has been the industry's standard dummy text ever since the 1500s, when an unknown printer took a galley.</p>
  <div class="service-grid">
    <div class="service-card" style="background:linear-gradient(135deg,#f06a2e,#c8461a)" role="img" aria-label="Mobile app development scene in orange tones">
      <span class="service-card__label" style="bottom:60px">iOS and Android<br>Development</span>
    </div>
    <div class="service-card" style="background:linear-gradient(135deg,#b36b78,#3d3b52)" role="img" aria-label="Laptop showing a website layout on a desk">
      <span class="service-card__label">Web Design</span>
    </div>
    <div class="service-card" style="background:linear-gradient(135deg,#43607c,#1d2b3c)" role="img" aria-label="Developer writing code at a computer">
      <span class="service-card__label">Software Development</span>
    </div>
    <div class="service-card" style="background:linear-gradient(135deg,#d8d2cc,#7f7671)" role="img" aria-label="Customer service team wearing headsets">
      <span class="service-card__label">Custom Service</span>
    </div>
  </div>
</section>

<section class="newsletter">
  <h2 class="section-title">Sign up for <span>our newsletter</span></h2>
  <p class="newsletter__sub">...and keep up with our latest news, upgrades and promotions!</p>
  <div class="newsletter__form">
    <div class="newsletter__input">User Name *</div>
    <div class="newsletter__input">User Email *</div>
    <a class="btn">Subscribe</a>
  </div>
</section>

<section class="news">
  <h2 class="section-title">Latest <span>News</span></h2>
  <div class="title-rule"></div>
  <article class="news-item" style="left:80px">
    <div class="news-item__thumb" role="img" aria-label="Person reading at a window"></div>
    <div>
      <h4 class="news-item__title">Lorem Ipsum is simply dummy text printing.</h4>
      <p class="news-item__text">Lorem Ipsum is simply dummy text of the text printing and typesetting industry.</p>
      <div class="news-item__meta"><span>▦ 31/08/2017</span><span style="color:#ccc">|</span><span>● Jon Reeve</span></div>
    </div>
  </article>
  <article class="news-item" style="left:626px">
    <div class="news-item__thumb" style="background:linear-gradient(135deg,#8fa7b8,#3f4e5c)" role="img" aria-label="Laptop screen with a web dashboard"></div>
    <div>
      <h4 class="news-item__title">Lorem Ipsum is simply dummy text printing.</h4>
      <p class="news-item__text">Lorem Ipsum is simply dummy text of the text printing and typesetting industry.</p>
      <div class="news-item__meta"><span>▦ 31/08/2017</span><span style="color:#ccc">|</span><span>● Jon Reeve</span></div>
    </div>
  </article>
</section>

<section class="career">
  <div class="photo career__bg" role="img" aria-label="Pale teal city backdrop"></div>
  <div class="photo career__person" role="img" aria-label="Cheerful man holding a laptop and a phone"></div>
  <h2 class="section-title">Our <span>Career</span></h2>
  <div class="career__rule"></div>
  <p class="body-copy">Lorem Ipsum is simply dummy text of the printing and typesetting industry. Lorem Ipsum has been the industry's standard dummy text ever since the 1500s, when an unknown printer took a galley of type and scrambled.</p>
  <div class="career__actions" style="top:300px">
    <a class="btn btn--outline">Send resume</a><a class="btn btn--outline">Coverletter</a><a class="btn">Apply now</a>
  </div>
</section>

<footer class="site-footer">
  <div class="footer-brand"><span class="brand__name">Vardek Hub</span><span class="brand__dot"></span></div>
  <div class="social" aria-label="Social links"><span class="social__item"></span><span class="social__item"></span><span class="social__item"></span></div>
  <nav class="footer-nav"><span>Home</span><span>About Us</span><span>Services</span><span>Career</span><span>Contact Us</span></nav>
  <p class="footer-legal"><b>© Vardek Hub</b> - 2017 All rights reserved | Terms and Conditions | Privacy policy</p>
</footer>

</body>
</html>
```